Shopping center investment profile

We need to design a two-page 8.5" x 11" brochure that can be used as a template for profiling our shopping centers and demonstrating our track record to investors.

Our company (KVM Real Estate Investments) owns retail shopping centers in the southwestern United States. Our website is www.kvmtrh.example, but we will be redesigning and modernizing the website and logo in the near future, so please do not use the color schemes or framework of the website for the brochure.

Our investors are institutional and high net worth investors who typically have an existing relationship with our company. They are determining whether to invest multi-millions of dollars in a shopping center opportunity, so the brochure needs to be professional, very high quality and provide key information about the specific property.
Updates

Additional guidance on color scheme:

We would like to see a Blue (something like Hex #5A61BC) and Gold (Hex #EDB215) or (Hex #DDA24B) color scheme with some Black accents 

Thank you!

Target Market(s)

Our target audiences are institutional investors, high net-worth individuals, financial firms and medium to large commercial real estate companies.

Industry/Entity Type

Investment

Requirements
Must have
• Clean and modern look with corresponding fonts and colors.
• Incorporates the information found in the attached "Marlowe Crossing profile" Pages or PDF file.
• Final file design files that can be modified easily
Nice to have
• Two examples of industry brochures are attached. These are examples of the professional quality that we are looking for, not necessarily the design or format.

```html
<!DOCTYPE html>
<html lang="en">
<head>
<meta charset="utf-8">
<title>Marlowe Crossing – Property Profile</title>
<link href="https://fonts.googleapis.com/css2?family=Questrial&family=Open+Sans:wght@400;600;700&family=Montserrat:wght@600&display=swap" rel="stylesheet">
<style>
:root{
  --blue:#525386;
  --gold:#dfb024;
  --black:#17171c;
  --white:#ffffff;
  --grey:#8a8c99;
  --stage:#d9d9db;
  --panel-text:#d8d8de;
}
*{margin:0;padding:0;box-sizing:border-box}
html,body{width:1200px;height:900px;overflow:hidden;background:var(--stage)}
.sheet-wrap{position:absolute;left:268px;top:21px;width:664px;height:858px}
.sheet{position:absolute;left:0;top:0;width:540px;height:698px;background:var(--white);
  transform:scale(1.2289);transform-origin:0 0;overflow:hidden;
  font-family:"Questrial",sans-serif;color:var(--black);box-shadow:0 2px 8px rgba(0,0,0,.15)}
.shapes{position:absolute;left:0;top:0;width:540px;height:698px}
.abs{position:absolute}
.title-block{left:0;top:0;width:218px;height:70px;background:var(--blue);color:var(--white);
  text-align:right;padding:12px 8px 0 0;font-size:23px;line-height:29px;letter-spacing:.5px}
.profile-title{left:238px;top:12px;font-size:24px;color:var(--blue);letter-spacing:.5px}
.profile-bar{left:238px;top:50px;width:218px;height:16px;background:var(--gold)}
.site-address{left:240px;top:78px;font-size:8.5px;line-height:10px;color:var(--grey);letter-spacing:.6px;text-transform:uppercase}

.summary{left:13px;top:348px;width:260px;color:var(--panel-text)}
.panel-heading{font-size:15px;color:var(--white);letter-spacing:.6px;line-height:18px}
.data-row{display:flex;font-size:9.3px;line-height:12.3px}
.data-row .label{width:122px}
.data-row .sep{width:8px}
.data-row .value{color:var(--white)}
.data-row strong{font-family:"Open Sans",sans-serif;font-weight:700;font-size:9px}
.rule{height:1px;background:#8d8d96}
.invest .data-row{line-height:10.7px}
.invest .data-row .label{width:122px}
.cash-heading{font-size:13px;line-height:15px;color:var(--white);letter-spacing:.5px}
.split{font-size:9px;line-height:11px}

.opportunity{left:284px;top:316px;width:226px;font-family:"Open Sans",sans-serif}
.opportunity h2{font-size:20px;font-weight:700;text-align:right;letter-spacing:.8px;padding-right:2px;line-height:24px}
.opportunity h3{font-size:23px;font-weight:700;text-align:right;line-height:28px;margin-top:10px;padding-right:2px}
.bullets{list-style:none;margin-top:4px}
.bullets li{font-size:7.2px;line-height:10.2px;padding-left:8px;position:relative;color:#1d1d22}
.bullets li::before{content:"";position:absolute;left:0;top:3.6px;width:3.4px;height:3.4px;border-radius:50%;background:#1d1d22}

.tagline{left:8px;top:669px;font-family:"Montserrat",sans-serif;font-weight:600;font-size:10.5px;color:var(--white);letter-spacing:.3px}
.brand{left:217px;top:622px;width:72px;height:58px;border-radius:50%;background:var(--white);border:1.5px solid var(--gold);
  display:flex;align-items:center;justify-content:center;text-align:center;font-size:8.6px;line-height:10px;color:var(--black)}
.office{left:300px;top:662px;font-size:8.4px;line-height:10.5px;color:var(--white)}
.divider{left:404px;top:660px;width:1px;height:36px;background:var(--white)}
.contact{left:410px;top:666px;font-size:8.4px;line-height:11px;color:var(--white)}
.contact span{display:inline-block;width:34px}
</style>
</head>
<body>
<div class="sheet-wrap">
  <div class="sheet">
    <svg class="shapes" viewBox="0 0 540 698" aria-hidden="false">
      <defs>
        <linearGradient id="photoTone" x1="0" y1="0" x2="1" y2="1">
          <stop offset="0" stop-color="#3f5a86"/>
          <stop offset=".45" stop-color="#9fb0c6"/>
          <stop offset=".75" stop-color="#9a6a4c"/>
          <stop offset="1" stop-color="#5e3a2a"/>
        </linearGradient>
      </defs>
      <path role="img" aria-label="Photo of the shopping center storefronts with signage under a cloudy sky"
            d="M0 70 H218 V100 H540 V262 L283 372 L0 266 Z" fill="url(#photoTone)"/>
      <polygon points="0,258 283,365 283,372 0,266" fill="var(--gold)"/>
      <polygon points="0,266 283,372 283,498 92,650 0,650" fill="var(--black)"/>
      <polygon points="283,498 283,512 110,650 92,650" fill="var(--gold)"/>
      <path d="M276 326 Q280 262 372 262 L512 262 L512 616 L276 616 Z" fill="var(--gold)"/>
      <polygon points="512,272 540,262 540,650 512,616" fill="var(--blue)"/>
      <rect x="0" y="650" width="540" height="48" fill="var(--gold)"/>
    </svg>

    <div class="abs title-block">Marlowe<br>Crossing</div>
    <div class="abs profile-title">Property Profile</div>
    <div class="abs profile-bar"></div>
    <div class="abs site-address">SWC of Halvor Rd and Tamsen Rd<br>Gilbert, Arizona</div>

    <section class="abs summary">
      <h2 class="panel-heading">SUMMARY</h2>
      <div class="data-row"><span class="label">Property Type</span><span class="sep">:</span><span class="value"><strong>Shopping Center</strong></span></div>
      <div class="data-row"><span class="label">Size</span><span class="sep">:</span><span class="value">79,490 sq ft</span></div>
      <div class="data-row"><span class="label">Purchased</span><span class="sep">:</span><span class="value">April 2011</span></div>
      <div class="data-row"><span class="label">Total Investment</span><span class="sep">:</span><span class="value">$X,XXX,XXX</span></div>
      <div class="data-row"><span class="label">Purchase Occupancy</span><span class="sep">:</span><span class="value">8.39%</span></div>
      <div class="data-row"><span class="label">Current Occupancy</span><span class="sep">:</span><span class="value">97.29%</span></div>
      <div class="data-row"><span class="label" style="width:auto">Projected 5-year IRR (Unleveraged) XX.XX%</span></div>
      <div class="rule" style="width:226px;margin:9px 0 10px"></div>
      <div class="invest">
        <h2 class="panel-heading">INVESTMENT INFORMATION</h2>
        <div class="data-row"><span class="label">Purchase Price</span><span class="value">$X,XXX,XXX</span></div>
        <div class="data-row"><span class="label">Sponsor Acquisition Fee</span><span class="value">$XX,XXX</span></div>
        <div class="data-row"><span class="label">Painting and Landscape</span><span class="value">$XXX,XXX</span></div>
        <div class="data-row"><span class="label">TI/LC Reserve</span><span class="value">$X,XXX,XXX</span></div>
        <div class="data-row"><span class="label">Operating Expenses</span><span class="value">$XXX,XXX</span></div>
      </div>
      <div class="rule" style="width:140px;margin:10px 0 9px"></div>
      <h2 class="cash-heading">TOTAL CASH<br>INVESTMENT</h2>
      <p class="split" style="margin-top:14px">Investor / Sponsor<br>Split&nbsp;&nbsp;&nbsp;XX% / XX%</p>
    </section>

    <section class="abs opportunity">
      <h2>OPPORTUNITY</h2>
      <ul class="bullets">
        <li>Bank owned property with attractive purchase price</li>
        <li>Strong relationship with seller’s broker and decision makers</li>
        <li>Redevelopment upside with management and leasing</li>
        <li>No major renovations required</li>
        <li>Gilbert location has very strong population, education and income demographics</li>
        <li>Adjacent to premier 2,500-residence master planned community of Cedar Vale Lakes</li>
        <li>Strong employment area with the new Halvorsen Gateway hospital and the adjacent Wrenfield Cancer center</li>
      </ul>
      <h3>Results</h3>
      <ul class="bullets">
        <li>Stabilized the shopping center within three years, producing excellent results for investors</li>
        <li>Transformed the center into a vibrant destination that the surrounding community is excited about</li>
        <li>Transitioned legacy tenants to upgrade the business operators</li>
        <li>Reduced the shopping center’s operating expenses by replacing vendors and appealing property taxes</li>
      </ul>
    </section>

    <div class="abs tagline">MAKING COMMUNITIES BETTER</div>
    <div class="abs brand">KVM<br>Real Estate<br>Investments</div>
    <div class="abs office">4400 East Tamsen Lane<br>Suite 210<br>Mesa, Arizona 85209</div>
    <div class="abs divider"></div>
    <div class="abs contact"><span>Phone</span>:&nbsp; 480-555-0142<br><span>Fax</span>:&nbsp; 480-555-0143</div>
  </div>
</div>
</body>
</html>
```